Business Card and Simple Logo Desgin

New Zealand based start up company "Brook Advisory LTD" requires business cards and simple logo design.

Card Content.

Brook Advisory LTD

Joanna Pritchard
CA, BMS (Hons)

j.pritchard@brookadvisory.co.nz
PH +64 21 574 160

Target Market(s)

Corporate Business in IT, Finance and accounting.

Industry/Entity Type

Business

```html
<!DOCTYPE html>
<html lang="en">
<head>
<meta charset="utf-8">
<title>Brook Advisory LTD – Business Card</title>
<link rel="stylesheet" href="https://fonts.googleapis.com/css2?family=Mulish:wght@400;800&display=swap">
<style>
  :root {
    --page-bg: #ffffff;
    --card-bg: #f2f2f2;
    --brand-green: #00b140;
    --ink: #1c1c1c;
    --on-green: #ffffff;
  }
  html, body {
    margin: 0;
    padding: 0;
    width: 900px;
    height: 1200px;
    overflow: hidden;
    background: var(--page-bg);
    font-family: "Mulish", sans-serif;
  }
  .canvas {
    position: relative;
    width: 900px;
    height: 1200px;
  }
  .card {
    position: absolute;
    left: 151px;
    top: 108px;
    width: 576px;
    height: 1005px;
    background: var(--card-bg);
    overflow: hidden;
  }
  .brand {
    position: absolute;
    left: 45px;
    top: 190px;
  }
  .brand-wordmark {
    margin: 0;
    font-size: 118px;
    font-weight: 800;
    line-height: 1;
    letter-spacing: -2px;
    color: var(--brand-green);
  }
  .brand-name {
    margin: 6px 0 0 0;
    font-size: 29px;
    font-weight: 400;
    letter-spacing: 0.3px;
    color: var(--ink);
    text-transform: uppercase;
  }
  .contact-band {
    position: absolute;
    left: 0;
    bottom: 0;
    width: 100%;
    height: 281px;
    background: var(--brand-green);
    color: var(--on-green);
    box-sizing: border-box;
    padding: 50px 0 0 33px;
  }
  .person-name {
    margin: 0;
    font-size: 34px;
    font-weight: 400;
    line-height: 1.2;
  }
  .person-credentials {
    margin: 2px 0 0 0;
    font-size: 20px;
    font-weight: 400;
  }
  .person-email {
    margin: 18px 0 0 0;
    font-size: 31px;
    font-weight: 400;
  }
  .person-phone {
    margin: 6px 0 0 0;
    font-size: 31px;
    font-weight: 400;
  }
  .phone-label {
    font-size: 20px;
    margin-right: 6px;
  }
</style>
</head>
<body>
  <main class="canvas">
    <article class="card">
      <header class="brand">
        <p class="brand-wordmark">brook</p>
        <p class="brand-name">Brook Advisory LTD</p>
      </header>
      <section class="contact-band">
        <p class="person-name">Joanna Pritchard</p>
        <p class="person-credentials">CA, BMS (Hons)</p>
        <p class="person-email">j.pritchard@brookadvisory.co.nz</p>
        <p class="person-phone"><span class="phone-label">Tel</span>+64 21 574 160</p>
      </section>
    </article>
  </main>
</body>
</html>
```